I need a podcast cover for a new podcast. The specs for the image should be should be 1400 x 1400 pixels, in JPG form, and under 500kb in size. It should be clearly readable when only around 200px wide. For inspiration, the podcast covers topics including men's grooming and fashion, food and cooking, travel, politics, fitness and finances.

Logo Text

The Harborwave

```html
<!DOCTYPE html>
<html lang="en">
<head>
<meta charset="utf-8">
<title>The Harborwave — Podcast Cover</title>
<link rel="stylesheet" href="https://fonts.googleapis.com/css2?family=Bebas+Neue&display=swap">
<style>
  :root {
    --page: #ffffff;
    --navy-deep: #03174a;
    --navy-light: #03377b;
    --mint: #2bffc4;
    --mint-shade: #26e6b2;
  }
  html, body {
    margin: 0;
    padding: 0;
    width: 1200px;
    height: 1199px;
    overflow: hidden;
    background: var(--page);
  }
  .cover {
    position: absolute;
    left: 129px;
    top: 128px;
    width: 952px;
    height: 952px;
    background: var(--navy-deep);
    overflow: hidden;
  }
  .backdrop {
    position: absolute;
    inset: 0;
    background: linear-gradient(90deg, var(--navy-light) 0%, var(--navy-light) 28%, var(--navy-deep) 62%, var(--navy-deep) 100%);
  }
  .mic-art {
    position: absolute;
    left: 100px;
    top: 242px;
    width: 271px;
    height: 514px;
    border-radius: 135px 135px 40px 40px;
    background: linear-gradient(180deg, var(--mint) 0%, var(--mint-shade) 100%);
  }
  .show-name {
    position: absolute;
    inset: 0;
    width: 952px;
    height: 952px;
  }
  .show-name text {
    font-family: "Bebas Neue", "Oswald", sans-serif;
    fill: var(--mint);
  }
</style>
</head>
<body>
  <main class="cover">
    <div class="backdrop" role="img" aria-label="Layered wavy contour lines in navy tones flowing down the cover"></div>
    <div class="mic-art" role="img" aria-label="Studio microphone on a stand in mint and white"></div>
    <svg class="show-name" viewBox="0 0 952 952" xmlns="http://www.w3.org/2000/svg" aria-label="The Harborwave">
      <text x="428" y="372" font-size="100">THE</text>
      <text x="424" y="548" font-size="214" textLength="431" lengthAdjust="spacingAndGlyphs">HARBOR</text>
      <text x="424" y="716" font-size="214">WAVE</text>
    </svg>
  </main>
</body>
</html>
```